Revamp Business Card for Landscaping/Gardening Service Provider

We are a small landscaping company that is in desperate need of someone to recreate our business card. I have attached what we are currently using along with the logo.

These are the services we specialize in:
- lawn service
- mow, edge and clean
- fertilizing
- prune and trim
- seed and topping
- planting
- irrigation sprinklers

We don't want the front to be too busy but we do want the bulk of the information to be on this side such as the logo (recreate if possible), what we do and maybe the contact information. The back we would like it to be lined if possible, to add notes or even provide quotes for customers. If you feel you've got the talent to take on this project, please send in your design.

Thank you

```html
<!DOCTYPE html>
<html lang="en">
<head>
<meta charset="utf-8">
<title>Ruben Castillo Gardening – Business Card</title>
<link rel="stylesheet" href="https://fonts.googleapis.com/css2?family=Montserrat:wght@800&family=Roboto:wght@400;500&display=swap">
<style>
  :root {
    --leaf: #4b7a2b;
    --ink: #1f1f1f;
    --muted: #7a7a7a;
    --paper: #ffffff;
    --backdrop: #e6e9e3;
  }
  * { margin: 0; padding: 0; box-sizing: border-box; }
  html, body { width: 1200px; height: 900px; overflow: hidden; }
  body { background: var(--backdrop); position: relative; font-family: "Roboto", Arial, sans-serif; color: var(--ink); }

  .card {
    position: absolute;
    width: 680px; height: 389px;
    background: var(--paper);
    overflow: hidden;
    box-shadow: 0 6px 18px rgba(0,0,0,.12);
  }
  .card--back { left: 260px; top: 36px; }
  .card--front { left: 260px; top: 475px; }
  .card__shapes { position: absolute; inset: 0; width: 100%; height: 100%; }
  .card__shapes path { fill: var(--leaf); }

  .brand { position: absolute; display: flex; align-items: center; gap: 12px; }
  .brand__mark { width: 54px; height: 54px; background: var(--leaf); flex: none; }
  .brand__name {
    font-family: "Montserrat", Arial, sans-serif; font-weight: 800;
    font-size: 23px; line-height: 1.05; text-transform: uppercase; color: var(--ink);
  }

  /* front */
  .card--front .brand { left: 38px; top: 28px; }
  .services { position: absolute; list-style: none; font-size: 14px; line-height: 1.45; color: var(--ink); }
  .services li::before { content: "- "; }
  .services--primary { left: 44px; top: 110px; }
  .services--secondary { left: 420px; top: 250px; }
  .services__heading {
    position: absolute; left: 230px; top: 212px;
    font-size: 17px; font-weight: 500; letter-spacing: .6px;
  }
  .contact { position: absolute; left: 400px; top: 34px; }
  .contact__name { font-size: 22px; color: var(--muted); margin-bottom: 8px; }
  .contact__line { display: flex; align-items: center; gap: 8px; font-size: 14px; line-height: 1.55; }
  .contact__line svg { width: 12px; height: 12px; fill: var(--ink); flex: none; }

  /* back */
  .card--back .brand { left: 0; right: 0; top: 70px; flex-direction: column; gap: 14px; }
  .card--back .brand__mark { width: 78px; height: 78px; }
  .card--back .brand__name { font-size: 28px; text-align: center; }
  .web { position: absolute; left: 150px; top: 232px; display: flex; align-items: center; gap: 14px; font-size: 15px; }
  .web__dot { width: 9px; height: 9px; border-radius: 50%; background: var(--muted); }
</style>
</head>
<body>

<section class="card card--back" aria-label="Card back">
  <svg class="card__shapes" viewBox="0 0 680 389" aria-hidden="true">
    <path d="M0,255 C170,305 370,240 520,300 C600,332 650,330 680,318 L680,389 L0,389 Z"/>
  </svg>
  <div class="brand">
    <span class="brand__mark"></span>
    <span class="brand__name">Ruben Castillo<br>Gardening</span>
  </div>
  <div class="web"><span class="web__dot"></span><span>www.castillogardening.com</span></div>
</section>

<section class="card card--front" aria-label="Card front">
  <svg class="card__shapes" viewBox="0 0 680 389" aria-hidden="true">
    <path d="M0,0 L55,0 C42,28 22,48 0,62 Z"/>
    <path d="M0,215 C120,228 205,300 290,389 L0,389 Z"/>
    <path d="M600,389 C618,352 648,336 680,330 L680,389 Z"/>
  </svg>

  <div class="brand">
    <span class="brand__mark"></span>
    <span class="brand__name">Ruben Castillo<br>Gardening</span>
  </div>

  <ul class="services services--primary">
    <li>lawn service</li>
    <li>mow, edge and clean</li>
    <li>fertilizing</li>
    <li>prune and trim</li>
  </ul>

  <div class="contact">
    <p class="contact__name">Ruben &amp; Elena Castillo</p>
    <p class="contact__line">
      <svg viewBox="0 0 24 24"><path d="M6.6 10.8a15.1 15.1 0 0 0 6.6 6.6l2.2-2.2a1 1 0 0 1 1-.25 11.4 11.4 0 0 0 3.6.57 1 1 0 0 1 1 1V20a1 1 0 0 1-1 1A17 17 0 0 1 3 4a1 1 0 0 1 1-1h3.5a1 1 0 0 1 1 1c0 1.25.2 2.45.57 3.57a1 1 0 0 1-.25 1z"/></svg>
      805 555 0142
    </p>
    <p class="contact__line">
      <svg viewBox="0 0 24 24"><path d="M2 5h20v14H2z M4 7v.5l8 5 8-5V7l-8 5z" fill-rule="evenodd"/></svg>
      info@castillogardening.com
    </p>
    <p class="contact__line">
      <svg viewBox="0 0 24 24"><path d="M12 2a10 10 0 1 0 0 20 10 10 0 0 0 0-20zm0 2c1.2 1.4 2 3.5 2.2 7H9.8C10 7.5 10.8 5.4 12 4zM4.1 11a8 8 0 0 1 4.3-6.1A13 13 0 0 0 7.8 11zm0 2h3.7c.1 2.4.5 4.4 1.3 6.1A8 8 0 0 1 4.1 13zm5.7 0h4.4c-.2 3.5-1 5.6-2.2 7-1.2-1.4-2-3.5-2.2-7zm6.4 0h3.7a8 8 0 0 1-4.3 6.1c.6-1.7 1-3.7.6-6.1zm0-2a13 13 0 0 0-.6-6.1A8 8 0 0 1 19.9 11z"/></svg>
      www.castillogardening.com
    </p>
  </div>

  <p class="services__heading">These are the services we specialize in:</p>

  <ul class="services services--secondary">
    <li>seed and topping</li>
    <li>planting</li>
    <li>irrigation sprinklers</li>
  </ul>
</section>

</body>
</html>
```